Q & Q Fabrications HVAC Mechanical Contractor Business Card

We need a business card for a HVAC/Plumbing Mechanical Contractor. Our website is http://www.qqfabrications-example.com. We would like to include the picture of the person on the card. Pictures of people for mock-ups can be found on our website. The blue on our logo is our primary color. We'd like this to be bold yet professional without too many colors but with some color to make sure it stands out.

Industry/Entity Type

Business

Contact Information for Business Card

Font styles to use
Sans Serif

Colors
000000

Requirements
Must have
• Our logo
• Person's picture
• Company Name
• Company Phone
• Person's email address
• Person's phone number
Nice to have
• Company Address
Should not have
• Clip art

```html
<!DOCTYPE html>
<html lang="en">
<head>
<meta charset="utf-8">
<title>Q &amp; Q Fabrications – Business Card</title>
<link href="https://fonts.googleapis.com/css2?family=Exo+2:wght@400;500;600;700&display=swap" rel="stylesheet">
<style>
  :root {
    --ink: #0b0b0b;
    --paper: #f4f4f4;
    --brand-blue: #4f97cf;
    --text-dark: #1c1c1c;
    --stage: #d9d6d1;
  }
  * { box-sizing: border-box; margin: 0; padding: 0; }
  html, body {
    width: 1200px; height: 818px; overflow: hidden;
    background: var(--stage);
    font-family: "Exo 2", sans-serif;
  }
  .stage {
    width: 1200px; height: 818px;
    display: flex; align-items: center; justify-content: center;
  }
  .card {
    width: 1000px; height: 572px;
    background: var(--paper);
    display: flex; flex-direction: column;
    box-shadow: 0 6px 18px rgba(0,0,0,.25);
  }
  .band-top {
    background: var(--ink); color: #fff;
    height: 150px; padding: 22px 56px 0;
  }
  .company-name {
    font-size: 54px; font-weight: 700; letter-spacing: 0.5px; line-height: 1.05;
  }
  .company-tagline {
    font-size: 40px; font-weight: 500; line-height: 1.2;
  }
  .card-body {
    flex: 1; display: flex; padding: 26px 56px 0;
  }
  .brand-column { width: 380px; }
  .brand-mark {
    width: 360px; height: 210px;
    border: 6px solid var(--ink);
    display: flex; align-items: center; justify-content: center; gap: 16px;
    background: #fff;
  }
  .brand-mark .square {
    width: 46px; height: 46px; background: var(--brand-blue);
  }
  .brand-mark .brand-name {
    font-size: 34px; font-weight: 700; color: var(--ink); line-height: 1.1;
  }
  .website {
    margin-top: 12px; font-size: 23px; font-weight: 600; color: var(--brand-blue);
  }
  .contact-column { padding-left: 48px; padding-top: 4px; }
  .person-name {
    font-size: 34px; font-weight: 700; color: var(--brand-blue); line-height: 1.1;
  }
  .person-title {
    font-size: 24px; font-weight: 500; color: var(--text-dark); margin-bottom: 14px;
  }
  .contact-list { list-style: none; }
  .contact-list li {
    display: flex; align-items: center; gap: 16px;
    font-size: 24px; color: var(--text-dark); line-height: 1.55;
  }
  .contact-list svg { width: 22px; height: 22px; fill: var(--brand-blue); flex: none; }
  .band-bottom {
    background: var(--ink); color: #fff;
    height: 92px; padding: 0 56px;
    display: flex; align-items: center;
    font-size: 26px; font-weight: 500;
  }
</style>
</head>
<body>
<main class="stage">
  <article class="card">
    <header class="band-top">
      <h1 class="company-name">Q&amp;Q FABRICATIONS, INC.</h1>
      <p class="company-tagline">Mechanical Contractor</p>
    </header>

    <section class="card-body">
      <div class="brand-column">
        <div class="brand-mark">
          <span class="square"></span>
          <span class="brand-name">Q&amp;Q<br>Fabrications</span>
        </div>
        <p class="website">www.qqfabrications-example.com</p>
      </div>

      <div class="contact-column">
        <h2 class="person-name">Dale Marsh</h2>
        <p class="person-title">Head of IT Services</p>
        <ul class="contact-list">
          <li>
            <svg viewBox="0 0 24 24" aria-hidden="true"><path d="M7 1h10a2 2 0 0 1 2 2v18a2 2 0 0 1-2 2H7a2 2 0 0 1-2-2V3a2 2 0 0 1 2-2zm0 3v13h10V4zm5 15a1.2 1.2 0 1 0 0 2.4A1.2 1.2 0 0 0 12 19z"/></svg>
            555-014-2281
          </li>
          <li>
            <svg viewBox="0 0 24 24" aria-hidden="true"><path d="M6.6 10.8a15.1 15.1 0 0 0 6.6 6.6l2.2-2.2a1 1 0 0 1 1-.25 11.4 11.4 0 0 0 3.6.57 1 1 0 0 1 1 1V20a1 1 0 0 1-1 1A17 17 0 0 1 3 4a1 1 0 0 1 1-1h3.5a1 1 0 0 1 1 1 11.4 11.4 0 0 0 .57 3.6 1 1 0 0 1-.25 1z"/></svg>
            555-014-3390
          </li>
          <li>
            <svg viewBox="0 0 24 24" aria-hidden="true"><path d="M6 2h10l3 3v4H6zm-3 8h18a1 1 0 0 1 1 1v8a1 1 0 0 1-1 1H3a1 1 0 0 1-1-1v-8a1 1 0 0 1 1-1zm3 3v2h3v-2zm5 0v2h3v-2zm5 0v2h3v-2z"/></svg>
            555-014-7716
          </li>
          <li>
            <svg viewBox="0 0 24 24" aria-hidden="true"><path d="M2 5h20v14H2zm2 2v.5l8 5 8-5V7zm0 2.8V17h16V9.8l-8 5z"/></svg>
            dmarsh@qqfabrications-example.com
          </li>
        </ul>
      </div>
    </section>

    <footer class="band-bottom">
      1450 Harlow Road, Fairview, WI 53000-0000
    </footer>
  </article>
</main>
</body>
</html>
```